Business card - Harbourline Stoneworks

Design a business card utilizing the given logo.
colors we like: Black, greys, Teal, blues.
Tri color card, horizontal orientation likely
Logo and name likely best on top.
Info on card:

Dennis Farrowby
#5 - 4180 Maple Ridge Blvd.
Surrey, B.C. V3K 2R9

778.555.0193
dennisfarrowby@brellnet.ca

Slogan: "Building Dreams"

We are a construction company that specializes in new home construction on the West coast of BC Canada. Open Concepts designs of high end homes.

```html
<!DOCTYPE html>
<html lang="en">
<head>
<meta charset="utf-8">
<title>Harbourline Stoneworks – Business Card</title>
<link rel="stylesheet" href="https://fonts.googleapis.com/css2?family=Carlito:wght@400;700&display=swap">
<style>
  :root {
    --page-bg: #e6e6e6;
    --card-bg: #ffffff;
    --ink: #2e2e2e;
    --ink-soft: #444444;
    --brand-grey: #3a3a3a;
    --band: #000000;
    --band-text: #ffffff;
    --rule: #555555;
  }
  html, body {
    margin: 0;
    padding: 0;
    width: 1200px;
    height: 1000px;
    overflow: hidden;
    background: var(--page-bg);
    font-family: "Carlito", "Calibri", sans-serif;
  }
  .card {
    position: absolute;
    left: 116px;
    top: 218px;
    width: 968px;
    height: 564px;
    background: var(--card-bg);
    box-shadow: 0 4px 18px rgba(0,0,0,0.18);
  }
  .brand {
    position: absolute;
    left: 184px;
    top: 100px;
    height: 110px;
    display: flex;
    align-items: center;
  }
  .brand-dot {
    width: 110px;
    height: 110px;
    border-radius: 50%;
    background: var(--brand-grey);
  }
  .brand-rule {
    width: 2px;
    height: 110px;
    background: var(--rule);
    margin: 0 34px 0 40px;
  }
  .brand-name {
    color: var(--brand-grey);
    font-weight: 400;
    letter-spacing: 2px;
    line-height: 1;
    text-transform: uppercase;
  }
  .brand-name .line-1 { display: block; font-size: 68px; }
  .brand-name .line-2 { display: block; font-size: 34px; letter-spacing: 5px; margin-top: 6px; text-align: right; }
  .title-band {
    position: absolute;
    left: 0;
    top: 282px;
    width: 100%;
    height: 64px;
    background: var(--band);
    color: var(--band-text);
    font-weight: 700;
    font-size: 32px;
    line-height: 64px;
    text-align: center;
  }
  .slogan {
    position: absolute;
    left: 0;
    top: 366px;
    width: 100%;
    text-align: center;
    color: var(--ink);
    font-size: 36px;
    line-height: 48px;
  }
  .address, .contact {
    position: absolute;
    left: 0;
    width: 100%;
    text-align: center;
    color: var(--ink-soft);
    font-size: 26px;
    line-height: 36px;
  }
  .address { top: 458px; }
  .contact {
    top: 498px;
    display: flex;
    justify-content: center;
    align-items: center;
    gap: 10px;
  }
  .contact svg { display: block; }
  .contact .gap { width: 8px; }
</style>
</head>
<body>
  <div class="card">
    <div class="brand">
      <div class="brand-dot"></div>
      <div class="brand-rule"></div>
      <div class="brand-name">
        <span class="line-1">Harbourline</span>
        <span class="line-2">Stoneworks</span>
      </div>
    </div>

    <div class="title-band">Dennis Farrowby / Chief Executive</div>

    <div class="slogan">Building Dreams</div>

    <div class="address">#5 - 4180 Maple Ridge Blvd.Surrey, B.C. V3K 2R9</div>

    <div class="contact">
      <svg width="22" height="18" viewBox="0 0 22 18" aria-hidden="true">
        <path d="M2 6 Q11 0 20 6 L18 9 L15 7 L15 5 Q11 3.5 7 5 L7 7 L4 9 Z" fill="#444"/>
        <rect x="5" y="9" width="12" height="8" rx="1.5" fill="#444"/>
      </svg>
      <span>778.555.0193</span>
      <span class="gap"></span>
      <svg width="20" height="14" viewBox="0 0 20 14" aria-hidden="true">
        <rect x="1" y="1" width="18" height="12" fill="none" stroke="#444" stroke-width="1.6"/>
        <path d="M1 1 L10 8 L19 1" fill="none" stroke="#444" stroke-width="1.6"/>
      </svg>
      <span>dennisfarrowby@brellnet.ca</span>
    </div>
  </div>
</body>
</html>
```